Tallow Crest Business Card

We need a business card designed for a a company called "Tallow Crest". We offer consulting, coaching and training to business leaders and coaches (across the world) using the latest findings in neuroscience, social and emotional intelligence and positive psychology. The final design should communicate the use of brain science to create sustainable relationships.

The card should be doublesided. The logo is attached and names and titles will be provided to the successful designer. Thank you.

Industry/Entity Type

Training

```html
<!DOCTYPE html>
<html lang="en">
<head>
<meta charset="utf-8">
<title>Tallow Crest Business Card</title>
<link rel="stylesheet" href="https://fonts.googleapis.com/css2?family=Exo+2:wght@800&family=Open+Sans:wght@400;700&display=swap">
<style>
  :root {
    --lime: #bcd72f;
    --lime-light: #d6ea3c;
    --charcoal: #2c2d2f;
    --sky: #1c9ad6;
    --white: #ffffff;
    --backdrop: #5b5b5b;
  }
  * { box-sizing: border-box; margin: 0; padding: 0; }
  html, body { width: 1200px; height: 900px; overflow: hidden; }
  body {
    background: var(--backdrop);
    font-family: "Open Sans", sans-serif;
    position: relative;
  }
  .card {
    position: absolute;
    left: 250px;
    width: 700px;
    height: 400px;
    overflow: hidden;
    box-shadow: 0 10px 30px rgba(0,0,0,0.35);
  }
  .card-front { top: 40px; }
  .card-back { top: 460px; }
  .card-art { position: absolute; inset: 0; width: 100%; height: 100%; }

  .brand {
    position: absolute;
    display: flex;
    align-items: center;
    gap: 12px;
    font-family: "Exo 2", sans-serif;
    font-weight: 800;
    text-transform: uppercase;
    letter-spacing: 1px;
    white-space: nowrap;
  }
  .brand-mark { border-radius: 50%; flex: none; }
  .card-front .brand {
    left: 0; right: 0; top: 170px;
    justify-content: center;
    color: var(--sky);
    font-size: 44px;
  }
  .card-front .brand-mark { width: 44px; height: 44px; background: var(--sky); }
  .card-back .brand {
    left: 30px; top: 300px;
    color: var(--white);
    font-size: 24px;
  }
  .card-back .brand-mark { width: 28px; height: 28px; background: var(--white); }

  .person {
    position: absolute;
    left: 40px; top: 64px;
    width: 275px;
    color: var(--white);
    font-family: "Exo 2", sans-serif;
    font-weight: 800;
    text-transform: uppercase;
    line-height: 1;
    white-space: nowrap;
  }
  .person-name { font-size: 40px; letter-spacing: 1px; }
  .person-title { font-size: 20px; margin-top: 4px; letter-spacing: 1px; }

  .divider {
    position: absolute;
    left: 335px; top: 66px;
    width: 2px; height: 90px;
    background: var(--white);
  }
  .contact {
    position: absolute;
    left: 352px; top: 68px;
    color: var(--white);
    font-size: 15px;
    line-height: 22px;
    list-style: none;
    white-space: nowrap;
  }
  .contact b { font-weight: 700; }
</style>
</head>
<body>

<section class="card card-front" aria-label="Card front">
  <svg class="card-art" viewBox="0 0 700 400" aria-hidden="true">
    <rect width="700" height="400" fill="var(--lime)"/>
    <path d="M0 105 C200 150 420 40 700 20 L700 265 C450 260 220 340 0 345 Z" fill="var(--charcoal)"/>
    <path d="M0 105 C200 150 420 40 700 20" fill="none" stroke="var(--sky)" stroke-width="7"/>
    <path d="M700 265 C450 260 220 340 0 345" fill="none" stroke="var(--sky)" stroke-width="9"/>
  </svg>
  <div class="brand"><span class="brand-mark"></span><span class="brand-name">Tallow Crest</span></div>
</section>

<section class="card card-back" aria-label="Card back">
  <svg class="card-art" viewBox="0 0 700 400" aria-hidden="true">
    <rect width="700" height="400" fill="var(--lime-light)"/>
    <path d="M0 0 L460 0 C560 30 640 60 700 90 L700 355 C450 300 200 250 0 200 Z" fill="var(--charcoal)"/>
    <path d="M460 0 C560 30 640 60 700 90" fill="none" stroke="var(--sky)" stroke-width="6"/>
    <path d="M700 355 C450 300 200 250 0 200" fill="none" stroke="var(--sky)" stroke-width="8"/>
  </svg>
  <div class="person">
    <p class="person-name">Rowan Pell</p>
    <p class="person-title">Director</p>
  </div>
  <div class="divider"></div>
  <ul class="contact">
    <li><b>Phone:</b> 555 014 227</li>
    <li><b>Website:</b> http://tallowcrest.example</li>
    <li><b>Email:</b> hello@tallowcrest.example</li>
    <li>Address Line, Your Company Address</li>
  </ul>
  <div class="brand"><span class="brand-mark"></span><span class="brand-name">Tallow Crest</span></div>
</section>

</body>
</html>
```